BUSINESS CARD DESIGN

NAME- TODD MASVERIK
PHONE NUMER - 808- 451-7082
EMAIL- OFFICE@VORLINDE-GRADEWAY.COM
BACK OF CARD- SPEACIALIZES IN LAND CLEARING, FORESTRY MUCLHING AND EXCAVATION

Contact Information for Business Card

NAME- TODD MASVERIK PHONE NUMER - 808- 451-7082 EMAIL- OFFICE@VORLINDE-GRADEWAY.COM BACK OF CARD- SPEACIALIZES IN LAND CLEARING , MUCLHING AND EXCAVATION

```html
<!DOCTYPE html>
<html lang="en">
<head>
<meta charset="utf-8">
<title>Vorlinde Gradeway LLC – Business Card</title>
<link href="https://fonts.googleapis.com/css2?family=Michroma&family=Open+Sans:wght@400;600;700&display=swap" rel="stylesheet">
<style>
  :root {
    --stage: #3a3a3a;
    --card-dark: #151515;
    --card-light: #ffffff;
    --ink: #111111;
    --silver: #d9d9d9;
    --accent: #f5b400;
    --muted: #2b2b2b;
  }
  * { box-sizing: border-box; margin: 0; padding: 0; }
  html, body { width: 1200px; height: 875px; overflow: hidden; }
  body {
    background: var(--stage);
    font-family: "Open Sans", sans-serif;
    position: relative;
  }
  .card {
    position: absolute;
    width: 540px;
    height: 308px;
    border-radius: 18px;
    overflow: hidden;
  }
  /* Back of card */
  .card-back {
    left: 40px;
    top: 283px;
    background: var(--card-dark);
    color: var(--silver);
  }
  .back-brand {
    position: absolute;
    left: 0; right: 0; top: 52px;
    display: flex;
    flex-direction: column;
    align-items: center;
    gap: 10px;
  }
  .brand-dot {
    width: 70px; height: 70px;
    border-radius: 50%;
    border: 3px solid var(--silver);
  }
  .brand-name {
    font-family: "Michroma", sans-serif;
    font-size: 22px;
    letter-spacing: 1px;
    color: var(--silver);
    text-align: center;
    line-height: 1.25;
  }
  .brand-sub {
    font-family: "Michroma", sans-serif;
    font-size: 11px;
    letter-spacing: 6px;
    color: var(--silver);
    text-align: center;
    border-top: 1px solid var(--silver);
    border-bottom: 1px solid var(--silver);
    padding: 4px 14px;
  }
  .brand-phone {
    font-family: "Michroma", sans-serif;
    font-size: 11px;
    letter-spacing: 7px;
    color: var(--silver);
  }
  .tagline {
    position: absolute;
    left: 0; right: 0; bottom: 26px;
    text-align: center;
    font-size: 12.5px;
    color: var(--accent);
    letter-spacing: .3px;
  }
  .tagline strong { font-weight: 700; }

  /* Front of card */
  .card-front {
    left: 620px;
    top: 283px;
    background: var(--card-light);
    color: var(--ink);
  }
  .front-mark {
    position: absolute;
    right: -90px; top: 20px;
    width: 260px; height: 260px;
    border-radius: 50%;
    background: var(--ink);
  }
  .front-brand {
    position: absolute;
    left: 34px; top: 34px;
  }
  .front-brand .brand-name { color: var(--ink); font-size: 20px; text-align: left; }
  .front-brand .brand-sub { color: var(--ink); border-color: var(--ink); margin-top: 6px; display: inline-block; }
  .front-brand .brand-phone { color: var(--ink); display: block; margin-top: 6px; }
  .accent-bar {
    position: absolute;
    left: 0; top: 150px;
    width: 10px; height: 46px;
    background: var(--accent);
  }
  .person {
    position: absolute;
    left: 34px; top: 150px;
  }
  .person-name {
    font-family: "Michroma", sans-serif;
    font-size: 20px;
    color: var(--ink);
    letter-spacing: .5px;
  }
  .person-title {
    font-size: 14px;
    color: var(--accent);
    margin-top: 2px;
  }
  .contacts {
    position: absolute;
    left: 34px; top: 212px;
    list-style: none;
    font-size: 11.5px;
    color: var(--muted);
    line-height: 1.35;
  }
  .contacts li { display: flex; align-items: flex-start; gap: 9px; margin-bottom: 3px; }
  .contacts svg { width: 12px; height: 12px; flex: none; margin-top: 2px; fill: var(--accent); }
</style>
</head>
<body>

<section class="card card-back" aria-label="Back of business card">
  <div class="back-brand">
    <span class="brand-dot" aria-hidden="true"></span>
    <div class="brand-name">VORLINDE GRADEWAY</div>
    <div class="brand-sub">LLC · HAWAII</div>
    <div class="brand-phone">808-451-7082</div>
  </div>
  <p class="tagline">SPEACIALIZES IN <strong>LAND CLEARING, MUCLHING &amp; EXCAVATION</strong></p>
</section>

<section class="card card-front" aria-label="Front of business card">
  <span class="front-mark" aria-hidden="true"></span>
  <div class="front-brand">
    <div class="brand-name">VORLINDE GRADEWAY</div>
    <div class="brand-sub">LLC · HAWAII</div>
    <span class="brand-phone">808-451-7082</span>
  </div>
  <span class="accent-bar" aria-hidden="true"></span>
  <div class="person">
    <div class="person-name">TODD MASVERIK</div>
    <div class="person-title">Founder &amp; CEO</div>
  </div>
  <ul class="contacts">
    <li>
      <svg viewBox="0 0 24 24" aria-hidden="true"><path d="M12 2a7 7 0 0 0-7 7c0 5 7 13 7 13s7-8 7-13a7 7 0 0 0-7-7zm0 9.5A2.5 2.5 0 1 1 12 6.5a2.5 2.5 0 0 1 0 5z"/></svg>
      <span>423 Street Address Here, City<br>State, Country, ZIP Code</span>
    </li>
    <li>
      <svg viewBox="0 0 24 24" aria-hidden="true"><path d="M6.6 10.8a15 15 0 0 0 6.6 6.6l2.2-2.2a1 1 0 0 1 1-.25 11.4 11.4 0 0 0 3.6.57 1 1 0 0 1 1 1V20a1 1 0 0 1-1 1A17 17 0 0 1 3 4a1 1 0 0 1 1-1h3.5a1 1 0 0 1 1 1c0 1.25.2 2.45.57 3.57a1 1 0 0 1-.25 1z"/></svg>
      <span>808- 451-7082</span>
    </li>
    <li>
      <svg viewBox="0 0 24 24" aria-hidden="true"><path d="M2 5h20v14H2zm2 2v.5l8 5 8-5V7l-8 5z"/></svg>
      <span>office@vorlinde-gradeway.com</span>
    </li>
    <li>
      <svg viewBox="0 0 24 24" aria-hidden="true"><path d="M12 2a10 10 0 1 0 0 20 10 10 0 0 0 0-20zm0 2c.9 1.2 1.6 2.6 2 4h-4c.4-1.4 1.1-2.8 2-4zM4.3 14a8 8 0 0 1 0-4h3.4a16 16 0 0 0 0 4zm5.7 0a14 14 0 0 1 0-4h4a14 14 0 0 1 0 4zm6.3 0a16 16 0 0 0 0-4h3.4a8 8 0 0 1 0 4zM12 20c-.9-1.2-1.6-2.6-2-4h4c-.4 1.4-1.1 2.8-2 4z"/></svg>
      <span>vorlinde-gradeway.com</span>
    </li>
  </ul>
</section>

</body>
</html>
```